Brintell's Business Card

I need some designs for a new business card including the new logo attached. An old example of our business card is also attached to show all the data that should be included on the new design.
**I added some more examples someone had mocked up**

Contact Information for Business Card

Should include all info on other examples uploaded.

```html
<!DOCTYPE html>
<html lang="en">
<head>
<meta charset="UTF-8">
<title>Brintell's Business Card</title>
<link href="https://fonts.googleapis.com/css2?family=Open+Sans:wght@400;600;700&display=swap" rel="stylesheet">
<style>
  :root {
    --backdrop: #3b3b3d;
    --card: #151516;
    --brand-blue: #1f74c9;
    --brand-red: #e0262b;
    --text-light: #e9e9e9;
    --gloss: #2c2c2e;
  }
  * { margin: 0; padding: 0; box-sizing: border-box; }
  html, body { width: 1200px; height: 801px; overflow: hidden; }
  body {
    background: var(--backdrop);
    font-family: "Open Sans", Arial, sans-serif;
    position: relative;
  }
  .card {
    position: absolute;
    top: 252px;
    width: 525px;
    height: 300px;
    background: var(--card);
    border-bottom: 3px solid var(--brand-blue);
    color: var(--text-light);
    overflow: hidden;
  }
  .card--front { left: 45px; }
  .card--back { left: 630px; }

  /* Front */
  .brand {
    position: absolute;
    left: 28px; top: 96px;
    width: 244px;
  }
  .brand__row { display: flex; align-items: center; gap: 10px; }
  .brand__dot {
    width: 28px; height: 28px; border-radius: 50%;
    background: var(--brand-blue); flex: none;
  }
  .brand__name {
    font-size: 32px; font-weight: 700; color: var(--brand-blue);
    line-height: 1; white-space: nowrap;
  }
  .brand__tagline {
    margin: 6px 0 0 38px;
    font-size: 7.5px; font-weight: 600; color: var(--brand-red);
    letter-spacing: 0.3px; white-space: nowrap;
  }
  .divider {
    position: absolute; left: 284px; top: 72px;
    width: 2px; height: 88px; background: var(--brand-blue);
  }
  .contact {
    position: absolute; left: 302px; top: 74px;
  }
  .contact__name {
    font-size: 20px; font-weight: 700; color: var(--brand-blue);
    margin-bottom: 10px; letter-spacing: 0.3px; white-space: nowrap;
  }
  .contact__line {
    display: flex; align-items: center; gap: 8px;
    font-size: 14px; margin-bottom: 6px; white-space: nowrap;
  }
  .contact__line svg { width: 12px; height: 12px; flex: none; }
  .credentials {
    position: absolute; left: 0; right: 0; bottom: 42px;
    text-align: center; font-size: 14px; letter-spacing: 0.4px;
  }
  .credentials__dot { color: var(--brand-red); margin: 0 8px; }

  /* Back */
  .emblem {
    position: absolute; left: 0; right: 0; top: 84px;
    display: flex; justify-content: center; align-items: center; gap: 10px;
  }
  .emblem__dot { width: 30px; height: 30px; border-radius: 50%; background: var(--gloss); }
  .emblem__name { font-size: 34px; font-weight: 700; color: var(--gloss); }
  .service-area {
    position: absolute; left: 0; right: 0; top: 196px;
    text-align: center; font-size: 15px;
  }
  .call-to-action {
    position: absolute; left: 0; right: 0; top: 222px;
    text-align: center; font-size: 14px; font-weight: 600; letter-spacing: 0.2px;
  }
</style>
</head>
<body>
  <section class="card card--front">
    <div class="brand">
      <div class="brand__row">
        <span class="brand__dot"></span>
        <span class="brand__name">BRINTELL'S</span>
      </div>
      <div class="brand__tagline">AIR CONDITIONING &amp; HEATING SERVICE</div>
    </div>
    <div class="divider"></div>
    <div class="contact">
      <div class="contact__name">DALTON BRINTELL</div>
      <div class="contact__line">
        <svg viewBox="0 0 24 24"><path fill="#e0262b" d="M6.6 10.8a15.2 15.2 0 0 0 6.6 6.6l2.2-2.2c.3-.3.7-.4 1-.2 1.1.4 2.3.6 3.6.6.6 0 1 .4 1 1V20c0 .6-.4 1-1 1A17 17 0 0 1 3 4c0-.6.4-1 1-1h3.5c.6 0 1 .4 1 1 0 1.2.2 2.4.6 3.6.1.3 0 .7-.2 1z"/></svg>
        <span>555.014.2287</span>
      </div>
      <div class="contact__line">
        <svg viewBox="0 0 24 24"><path fill="#e0262b" d="M2 5h20v14H2z"/><path fill="none" stroke="#151516" stroke-width="2" d="M2 5l10 8 10-8"/></svg>
        <span>hvacbrintell@mailbox.com</span>
      </div>
    </div>
    <div class="credentials">LICENSED &amp; INSURED<span class="credentials__dot">•</span>FAMILY OWNED &amp; OPERATED</div>
  </section>

  <section class="card card--back">
    <div class="emblem">
      <span class="emblem__dot"></span>
      <span class="emblem__name">BRINTELL'S</span>
    </div>
    <div class="service-area">Serves Maple Ridge, IA &amp; Surrounding Areas</div>
    <div class="call-to-action">CALL TODAY FOR ALL YOUR HVAC, REFRIGERATION &amp; PLUMBING NEEDS</div>
  </section>
</body>
</html>
```